Marla Hensley Book Cover

- 6x9 book cover.
- Book title: Unlearning the busy calendar trap - a widow's road from ruin to fortune
- Back cover will show the 3 testimonials along with their pictures ( we only have two atm, so please just leave a space for a 3rd ). Back cover will also include "about the author"
- Front cover to feature author's picture and background should have nature view ( outside window )
- Author's text: ( The language about me )
This is one woman’s story about her journey from the depths of despair to happiness and financial success. She stopped chasing the Busy-Calendar Trap. Marla shares the steps she then took to change her life.
Listed in Halvern Merit Registry, Prairie Ledger Honorees and more Marla Hensley provides hands on, real life advice to help you make remarkable changes in your life.

```html
<!DOCTYPE html>
<html lang="en">
<head>
<meta charset="utf-8">
<title>Marla Hensley Book Cover</title>
<link href="https://fonts.googleapis.com/css2?family=Anton&family=Comic+Neue:wght@400;700&family=Tinos:wght@400;700&display=swap" rel="stylesheet">
<style>
  :root {
    --stage: #111111;
    --paper: #ffffff;
    --ink: #111111;
    --rule: #333333;
    --accent: #e8742a;
    --spine-line: #c9c9c9;
    --placeholder: #7a7a7a;
    --ornament: #e9e9e9;
  }
  * { margin: 0; padding: 0; box-sizing: border-box; }
  html, body { width: 1200px; height: 1200px; overflow: hidden; background: var(--stage); }
  .canvas { position: relative; width: 1200px; height: 1200px; }

  .spread {
    position: absolute; left: 106px; top: 275px; width: 982px; height: 707px;
    background: var(--paper);
    box-shadow: 0 10px 30px rgba(0,0,0,.6);
  }

  /* back cover */
  .about-heading {
    position: absolute; left: 45px; top: 92px; width: 381px;
    display: flex; align-items: flex-end; gap: 4px;
    font: 700 12px/1 "Tinos", serif; color: var(--ink);
  }
  .about-heading::after { content: ""; flex: 1; border-bottom: 1px solid var(--rule); margin-bottom: 1px; }
  .about-body {
    position: absolute; left: 45px; top: 116px; width: 400px;
    font: 400 12.2px/15.2px "Tinos", serif; color: var(--ink);
  }
  .testimonial-frame { position: absolute; left: 47px; width: 117px; }
  .testimonial-frame svg { display: block; }
  .quote {
    position: absolute; font: 400 10px/12.5px "Tinos", serif; color: var(--ink);
  }
  .quote strong { font-weight: 700; }

  /* spine */
  .spine {
    position: absolute; left: 470px; top: 0; width: 38px; height: 707px;
    border-left: 2px solid var(--spine-line); border-right: 2px solid var(--spine-line);
  }
  .spine-title {
    position: absolute; left: 50%; top: 177px;
    writing-mode: vertical-rl;
    transform: translateX(-50%);
    font: 400 21px/1 "Anton", sans-serif; color: var(--ink); white-space: nowrap;
  }

  /* front cover */
  .front { position: absolute; left: 508px; top: 0; width: 474px; height: 707px; overflow: hidden; }
  .ornament { position: absolute; top: 0; width: 118px; height: 112px; background: var(--ornament); }
  .ornament.left { left: 2px; }
  .ornament.right { right: 2px; }
  .front-title {
    position: absolute; left: 0; right: 0; top: 54px; text-align: center;
    font: 400 49px/56px "Anton", sans-serif; color: var(--ink);
  }
  .front-subtitle {
    position: absolute; left: 0; right: 0; top: 180px; text-align: center;
    font: 700 18px/1 "Comic Neue", sans-serif; color: var(--ink);
  }
  .accent-rule { position: absolute; left: 2px; right: 0; top: 206px; height: 2px; background: var(--accent); }
  .author-photo {
    position: absolute; left: 0; right: 0; top: 210px; bottom: 0;
    background: radial-gradient(ellipse 55% 60% at 52% 55%, #d9b79c 0%, #e6d3c0 45%, #f4efe9 75%, #ffffff 100%);
  }
</style>
</head>
<body>
<div class="canvas">
  <div class="spread">
    <section class="back">
      <h2 class="about-heading">The language about me</h2>
      <p class="about-body">This is one woman’s story about her journey from the depths of despair to happiness and financial success. She stopped chasing the Busy-Calendar Trap. Marla shares the steps she then took to change her life.<br>Listed in Halvern Merit Registry, Prairie Ledger Honorees and more Marla Hensley provides hands on, real life advice to help you make remarkable changes in your life.</p>

      <div class="testimonial-frame" style="top:266px">
        <svg width="117" height="120" viewBox="0 0 117 120">
          <polygon points="0,15 117,0 105,120 0,120" fill="#111"/>
          <rect x="0" y="15" width="104" height="104" fill="#a48473" role="img" aria-label="Portrait photo of Renata Colby"/>
        </svg>
      </div>
      <p class="quote" style="left:170px;top:309px;width:262px">“As a clarity, leadership &amp;communication strategist, I found Marla’s advice to be down to earth, providing a no-nonsense foundation to begin making the life changes women want.”<br><strong>Renata Colby,</strong> Author of the Quiet Ladder</p>

      <div class="testimonial-frame" style="top:391px">
        <svg width="117" height="120" viewBox="0 0 117 120">
          <polygon points="0,15 117,0 105,120 0,120" fill="#111"/>
          <rect x="0" y="15" width="104" height="104" fill="#7a5a44" role="img" aria-label="Portrait photo of Joelle Marsh"/>
        </svg>
      </div>
      <p class="quote" style="left:170px;top:418px;width:268px">As our world gets increasingly more stressful, the complexities of trying to develop true balance in our lives, work, and relationships adds more stress. In her book, Marla Hensley offers sound advice on how to create and maintain a healthy lifestyle.&nbsp; This book is a must have!<br><strong>Joelle Marsh,</strong> Harbor Tower Survivor, Meridian Post Best-Selling Author and Founder of The Common Table Project</p>

      <div class="testimonial-frame" style="top:522px">
        <svg width="117" height="120" viewBox="0 0 117 120">
          <polygon points="0,15 117,0 105,120 0,120" fill="#111"/>
          <rect x="0" y="15" width="104" height="104" fill="var(--placeholder)"/>
        </svg>
      </div>
    </section>

    <div class="spine">
      <span class="spine-title">Unlearning the busy calendar trap</span>
    </div>

    <section class="front">
      <div class="ornament left" role="img" aria-label="Decorative corner flourish"></div>
      <div class="ornament right" role="img" aria-label="Decorative corner flourish"></div>
      <h1 class="front-title">Unlearning the busy<br>calendar trap</h1>
      <p class="front-subtitle">a widow's road from ruin to fortune</p>
      <div class="accent-rule"></div>
      <div class="author-photo" role="img" aria-label="Portrait photo of author Marla Hensley"></div>
    </section>
  </div>
</div>
</body>
</html>
```